Marnie Vale Photography needs a unique, creative business card/logo design

I need a design for business cards/logo that is unique and creative in the industry. Simplicity is nice, so not too crowded. Something that will catch my customer's eye and remain in their memory. I am primarily a landscape photographer but will be soon may be branching into boudoir photography as well. I have attached my current card.

Marnie Vale Photography
Phone: 0439 517 264
Email: MarnieValePhotography@quillmail.example
Website: www.snapnook.example/MarnieValePhotography.Aust

Marnie Vale Photography

• Contact Details on one side
• pixelation

```html
<!DOCTYPE html>
<html lang="en">
<head>
<meta charset="utf-8">
<title>Marnie Vale Photography — Business Card</title>
<link rel="stylesheet" href="https://fonts.googleapis.com/css2?family=Playfair+Display:wght@700&family=Libre+Baskerville&display=swap">
<style>
  :root {
    --backdrop: #1c1c1e;
    --card-white: #f7f7f7;
    --card-white-shade: #e4e4e6;
    --card-dark: #262627;
    --teal: #2bbdc1;
    --ink: #4a4a4c;
    --sky-top: #e9e6e2;
    --sunset: #c98a55;
    --sand: #6a4434;
    --sand-deep: #3b2822;
  }
  * { margin: 0; padding: 0; box-sizing: border-box; }
  html, body {
    width: 1200px; height: 873px; overflow: hidden;
    background: var(--backdrop);
  }
  .stage {
    position: relative; width: 1200px; height: 873px;
    display: flex; align-items: center; justify-content: center; gap: 50px;
  }
  .card {
    position: relative; width: 530px; height: 303px;
    border-radius: 16px; overflow: hidden;
  }

  /* Brand lockup: plain ring above a stacked name */
  .brand {
    display: flex; flex-direction: column; align-items: center;
    color: var(--teal);
    font-family: "Playfair Display", serif; font-weight: 700;
  }
  .brand__ring {
    width: 66px; height: 66px; border-radius: 50%;
    border: 7px solid var(--teal);
    margin-bottom: 12px;
  }
  .brand__name { font-size: 30px; line-height: 1; letter-spacing: 0.5px; }
  .brand__sub {
    font-size: 10px; line-height: 1; letter-spacing: 7px;
    text-transform: uppercase; margin-top: 8px; padding-left: 7px;
  }

  /* Front: contact side */
  .card--front {
    background: linear-gradient(150deg, var(--card-white) 0%, #ffffff 45%, var(--card-white-shade) 100%);
  }
  .card--front .texture {
    position: absolute; inset: 0;
    background: linear-gradient(120deg, rgba(0,0,0,0) 0%, rgba(0,0,0,0.035) 50%, rgba(0,0,0,0) 100%);
  }
  .card--front .brand {
    position: absolute; left: 0; right: 0; top: 34px;
  }
  .contacts {
    position: absolute; left: 0; right: 0; bottom: 32px;
    font-family: "Libre Baskerville", serif; font-size: 12.5px; color: var(--ink);
    display: flex; flex-direction: column; align-items: center; gap: 12px;
  }
  .contacts__row { display: flex; gap: 30px; }
  .contact { display: flex; align-items: center; gap: 8px; white-space: nowrap; }
  .contact svg { flex: none; }
  .contact__dot { width: 11px; height: 11px; border-radius: 50%; background: var(--teal); flex: none; }

  /* Back: photo side */
  .card--back { background: var(--card-dark); }
  .photo {
    position: absolute; left: 0; top: 0; width: 62%; height: 100%;
    background:
      linear-gradient(90deg, rgba(38,38,39,0) 55%, var(--card-dark) 100%),
      linear-gradient(180deg, var(--sky-top) 0%, #cfc9c2 38%, var(--sunset) 47%, var(--sand) 55%, var(--sand-deep) 100%);
  }
  .card--back .sheen {
    position: absolute; inset: 0;
    background: linear-gradient(160deg, rgba(255,255,255,0.12) 0%, rgba(255,255,255,0) 40%);
  }
  .card--back .brand {
    position: absolute; right: 34px; top: 62px;
  }
</style>
</head>
<body>
<main class="stage">
  <section class="card card--front" aria-label="Business card, contact side">
    <div class="texture" role="img" aria-label="Faint light-grey faceted texture"></div>
    <div class="brand">
      <span class="brand__ring"></span>
      <span class="brand__name">Marnie Vale</span>
      <span class="brand__sub">Photography</span>
    </div>
    <div class="contacts">
      <div class="contacts__row">
        <div class="contact">
          <svg width="14" height="14" viewBox="0 0 24 24" aria-hidden="true"><path fill="var(--teal)" d="M6.6 10.8a15 15 0 0 0 6.6 6.6l2.2-2.2a1 1 0 0 1 1-.25 11.4 11.4 0 0 0 3.6.57 1 1 0 0 1 1 1V20a1 1 0 0 1-1 1A17 17 0 0 1 3 4a1 1 0 0 1 1-1h3.5a1 1 0 0 1 1 1c0 1.250.2 2.450.57 3.57a1 1 0 0 1-.25 1z"/></svg>
          <span>+61 439 517 264</span>
        </div>
        <div class="contact">
          <svg width="16" height="12" viewBox="0 0 16 12" aria-hidden="true"><rect x="0.5" y="0.5" width="15" height="11" rx="1" fill="var(--teal)"/><path d="M1 1l7 5.5L15 1" fill="none" stroke="#fff" stroke-width="1.2"/></svg>
          <span>m-vale@quillmail.example</span>
        </div>
      </div>
      <div class="contact">
        <span class="contact__dot"></span>
        <span>/MarnieValePhotography.Aust/</span>
      </div>
    </div>
  </section>

  <section class="card card--back" aria-label="Business card, photo side">
    <div class="photo" role="img" aria-label="Photograph of a spiral seashell on a sandy beach at sunset with calm water behind"></div>
    <div class="sheen"></div>
    <div class="brand">
      <span class="brand__ring"></span>
      <span class="brand__name">Marnie Vale</span>
      <span class="brand__sub">Photography</span>
    </div>
  </section>
</main>
</body>
</html>
```